Copper Lantern needs Stationary and Business Cards
Designs needs
Traditional
Delia R. Stroup
Owner
482 W. Hollin Creek Rd.
Marlow Falls, MI 49012
stroupd@lantern482.com
www.lantern482.com
What colors would you like? Black and Burnt Red
The Tavern will have an industrial chic style (updated vintage). I have attached a few clipart elements

```html
<!DOCTYPE html>
<html lang="en">
<head>
<meta charset="utf-8">
<title>Copper Lantern — Business Cards</title>
<link rel="stylesheet" href="https://fonts.googleapis.com/css2?family=Old+Standard+TT:wght@400;700&display=swap">
<style>
  :root {
    --backdrop: #d9d6d1;
    --paper: #efe4c2;
    --paper-edge: #ddc999;
    --ink: #1d1a17;
    --burnt-red: #7e2a1c;
    --hand-tone: #c9b78f;
    --hand-shade: #8d7b5c;
  }
  * { box-sizing: border-box; margin: 0; padding: 0; }
  html, body { width: 1200px; height: 866px; overflow: hidden; }
  body {
    background: var(--backdrop);
    position: relative;
    font-family: "Old Standard TT", Georgia, serif;
    color: var(--ink);
  }
  .card {
    position: absolute;
    width: 617px;
    height: 346px;
    background: radial-gradient(ellipse at 45% 45%, var(--paper) 55%, var(--paper-edge) 100%);
    box-shadow: 0 6px 16px rgba(0,0,0,0.25);
    overflow: hidden;
  }
  .card--front { left: 115px; top: 67px; }
  .card--back { left: 473px; top: 466px; }

  .wordmark {
    position: absolute;
    display: flex;
    align-items: center;
    justify-content: center;
    font-weight: 700;
    color: var(--ink);
    text-transform: uppercase;
    line-height: 1.05;
    letter-spacing: 1px;
    text-align: center;
    font-size: 42px;
  }
  .card--front .wordmark { left: 39px; top: 24px; width: 235px; height: 226px; }
  .card--back .wordmark { left: 317px; top: 41px; width: 235px; height: 235px; }

  .pointing-hand {
    position: absolute;
    background: linear-gradient(160deg, var(--hand-tone), var(--hand-shade));
    opacity: 0.85;
  }
  .card--front .pointing-hand { left: 312px; top: 24px; width: 293px; height: 149px; border-radius: 60px 10px 10px 40px; }
  .card--back .pointing-hand { left: 0; top: 91px; width: 295px; height: 163px; border-radius: 0 60px 40px 0; }

  .holder {
    position: absolute;
    right: 22px;
    top: 222px;
    text-align: right;
    color: var(--burnt-red);
    font-variant: small-caps;
  }
  .holder__name { font-size: 26px; letter-spacing: 0.5px; line-height: 1.1; }
  .holder__title { font-size: 17px; margin-top: 2px; }

  .address {
    position: absolute;
    right: 22px;
    top: 293px;
    font-size: 13px;
    white-space: nowrap;
  }
  .contacts {
    position: absolute;
    right: 22px;
    top: 315px;
    font-size: 14px;
    display: flex;
    align-items: center;
    gap: 6px;
    white-space: nowrap;
  }
  .contacts svg { width: 14px; height: 14px; fill: var(--burnt-red); }
  .contacts .item { display: flex; align-items: center; gap: 4px; }

  .web {
    position: absolute;
    left: 317px;
    width: 235px;
    text-align: center;
    top: 284px;
    font-size: 16px;
    letter-spacing: 1px;
  }
</style>
</head>
<body>
  <section class="card card--front">
    <div class="wordmark">Copper<br>Lantern</div>
    <div class="pointing-hand" role="img" aria-label="Vintage engraving of a pointing hand"></div>
    <div class="holder">
      <div class="holder__name">Delia R. Stroup</div>
      <div class="holder__title">Owner</div>
    </div>
    <div class="address">482 W. Hollin Creek Rd. Marlow Falls, MI 49012</div>
    <div class="contacts">
      <span class="item">
        <svg viewBox="0 0 16 16" aria-hidden="true"><circle cx="8" cy="8" r="7.5" fill="none" stroke="#7e2a1c" stroke-width="1.2"/><path d="M5 4.5l1.5-.5 1 2-1 .8c.4 1 1.2 1.9 2.2 2.4l.8-1 2 1-.5 1.5c-3 .2-6.2-3-6-6.2z"/></svg>
        555.014.3870
      </span>
      <span class="sep">|</span>
      <span class="item">
        <svg viewBox="0 0 16 16" aria-hidden="true"><rect x="4" y="2" width="8" height="5"/><rect x="1.5" y="7" width="13" height="6" rx="1"/></svg>
        555.014.3875
      </span>
      <span class="sep">|</span>
      <span class="item">
        <svg viewBox="0 0 16 16" aria-hidden="true"><rect x="1" y="3.5" width="14" height="9" rx="1"/><path d="M1.5 4l6.5 5 6.5-5" fill="none" stroke="#efe4c2" stroke-width="1.2"/></svg>
        stroupd@lantern482.com
      </span>
    </div>
  </section>

  <section class="card card--back">
    <div class="pointing-hand" role="img" aria-label="Vintage engraving of a hand pointing right"></div>
    <div class="wordmark">Copper<br>Lantern</div>
    <div class="web">www.lantern482.com</div>
  </section>
</body>
</html>
```